Marlowe Vocation Advisors Trifold Flier/ Brochure

Trifold Paper and/or Digital brochure to outline range of Career Coaching, Topical Workshops/ Webinars, Experiential Education Program, Regional Professional Networking Events in Chesapeake Bay Area - particular focus on "students to seniors" thinking forward about sustainability focused issues, solutions, careers, leadership and entrepreneurship. Area of Service covers 6 states surrounding the Chesapeake Bay, representing many stakeholders from business to education, policy, envrionmental centers, ngo's etc. There is an iconic bridge that connects between urban and rural areas, and we hope to think of our work as "bridging" by building collaborative relationships between sectors, stakeholders, communities, age groups, etc... Also considering the bridge metaphor as important to creating pathways across varied stages across lifespan/ career ....thus students to senior level life/ education/ career/ leadership. Something like: , which may be depicted as "Education| Careers| Leadership - Partners for a Sustainable Future" . In terms of content, we hope to outline Services include Coaching/ Curriculum/ Community....Sustainability Focused Projects/ Partnerships...Thinking Globally, Acting Locally
Updates

Target Market(s)

Students from Regional Schools in various "sustainability" related programs, including Certified Green Schools, Community Colleges, Universities all seeking to translate their education to job opportunities. Also Professionals in various sectors/ professions who are seeking to transition new jobs emerging in areas that align with "sustainability"..i.e. energy, food supply chain, water, health, policy, .... Later life folks who are moving from classic jobs to phased retirement with interests in being more entrepreneurial - also bringing networks from their professional years and potential mentors to younger ones even while they themselves evolve...Overall, will be connecting to organizations to collaborate such as Chamber of Commerce, Coalition for Tidewater Marshes, Professional Associations, Community Projects who may host projects or opportunity for shared presentations, focused working groups, leadership programs wherein Marlowe Vocation Advisors will be collaborator.

Industry/Entity Type

Education

Font styles to use
Sans Serif

Colors
9bcb3c
00a990
0356a4
0692cd
fbed22

Requirements
Must have
• the triparte logo uploaded, originally designed within pixel guild in 2013!
• color scheme with predominate but "natural" looking green/ earth/ blues to relate to the "land/ water/ wildlife"...but also images that represent professions such as solar panels, or field based teams, as well as individualized coaching photos. See also website www.marlowevocationadvisors.com Clarity of Offerings - Coaching: Education Career & Leadership Levels, Curriculum: Customized Workshops/ Webinars/ Network Events, Community: Marlowe Steward Crossing Program(s).
Nice to have
• Clean Contemporary Fonts, Layout, Styling with Color Themes looking both "organic" and upscale professional at the same time. Able to print on very basic parchment paper as well as something magazine style...or just send digitally. Emphasis on Green Careers Images, and 1 to 1 coaching or mentoring...as well as some groups on location doing projects.
• Visual design/layout to connect the parts to a whole....i.e.Essentially Coaching/ Curriculum/ Community....Within this we see careers as a process/ pathway that requires partnerships...we focus on shared connector around sustainability focused professional areas. When we say "sustainability" we think.... People, Planet, Profitability....or Triple Bottom Line idea of Economy, Environment, Education/ Equity? you get the idea. The logo was designed to illustrate this triparte, but also the implication of "Thinking Globally/ Acting Locally"....(thus the globe, the local bay with sailboats & community, the leaves as our local lands) Hoping the trifold idea can be used to help segregate but also unify ideas here, with overarching logo?
• Also I have shared with you another "postcard" design that is related to our curriculum area...known as VocaTerrana. The program has 4 phases which we've shared with you to better understand, although this does NOT need to be overemphasized here. The mock up brochure and our website (although not very good design) offers example of pointing to this among other aspects, and we can then share other handouts for that detail as these pieces will work together.
Should not have
• Too many words, too much explanation,
• Busy-ness...

```html
<!DOCTYPE html>
<html lang="en">
<head>
<meta charset="utf-8">
<title>Marlowe Vocation Advisors – Trifold Flier</title>
<link rel="stylesheet" href="https://fonts.googleapis.com/css2?family=Questrial&family=Arimo:ital,wght@0,400;0,700;1,400;1,700&display=swap">
<style>
:root{
  --backdrop:#2b2b2b;
  --leaf:#8cbf3f;
  --leaf-soft:#a9cf55;
  --deep:#3d7d1f;
  --forest:#2f6a14;
  --lime:#d6e67a;
  --cream:#f7f9e6;
  --sky:#1a8fd0;
  --navy:#1f56a4;
  --ink:#1b1b1b;
  --white:#ffffff;
}
*{box-sizing:border-box;margin:0;padding:0}
html,body{width:885px;height:1200px;overflow:hidden;background:var(--backdrop)}
body{position:relative;font-family:"Arimo",Arial,sans-serif;color:var(--ink)}
.page{position:absolute;left:50px;width:768px;overflow:hidden;background:var(--white)}
.page-cover{top:47px;height:527px}
.page-inside{top:586px;height:526px}
.abs{position:absolute}
.center{text-align:center}

/* ---------- cover, left panel ---------- */
.intro-panel{left:0;top:0;width:390px;height:527px;overflow:hidden;
  background:linear-gradient(180deg,transparent 0,transparent 170px,var(--cream) 170px,var(--white) 100%)}
.intro-sky{left:0;top:0;width:390px;height:200px;
  background:linear-gradient(100deg,var(--deep) 0%,var(--leaf) 45%,var(--lime) 80%,#f2f4c6 100%)}
.intro-title{left:30px;top:4px;width:310px;font-family:"Questrial",sans-serif;font-size:27px;line-height:32px;
  color:var(--white);letter-spacing:.3px;white-space:nowrap;font-weight:400}
.intro-copy{left:6px;top:40px;width:228px;font-size:10px;line-height:1.3;color:var(--ink);font-weight:700}
.intro-copy .brand{color:var(--white);font-size:11.5px}
.intro-copy .soft{font-weight:400}
.intro-copy em{font-style:italic}
.intro-photo{left:240px;top:38px;width:142px;height:120px;
  background:linear-gradient(160deg,#4a3a2a,#c9b79b 55%,#e9dccb)}
.swoosh{left:0;top:140px;width:390px;height:80px}
.label-bar{background:linear-gradient(180deg,var(--leaf-soft),var(--leaf));border-radius:8px;color:var(--ink);font-weight:700;text-align:center}
.coach-bar{left:32px;top:207px;width:325px;height:40px;font-size:12px;line-height:1.3;padding-top:4px}
.team-list{left:20px;width:350px;font-size:9px;font-weight:700;line-height:1.75}
.team-coach{top:252px}
.program-head{left:30px;top:318px;width:330px;font-size:12px;font-weight:700;color:var(--forest);line-height:1.2;border-bottom:1px solid var(--forest);padding-bottom:3px}
.team-program{top:354px}
.call-box{left:32px;top:408px;width:302px;height:112px;border-radius:8px;
  background:linear-gradient(180deg,var(--leaf-soft) 0%,var(--lime) 40%,var(--cream) 100%)}
.call-head{left:0;top:5px;width:302px;font-size:11px;font-weight:700;color:var(--forest)}
.call-info{left:0;top:21px;width:302px;font-size:10px;line-height:1.15}
.call-info b{font-weight:700}
.url-pill{background:var(--ink);color:var(--white);border-radius:10px;font-size:10px;font-weight:700;font-style:italic;text-align:center}
.call-url{left:24px;top:86px;width:254px;height:20px;line-height:20px}

/* ---------- cover, right panel ---------- */
.cover-panel{left:390px;top:0;width:378px;height:527px;background:var(--white);overflow:hidden}
.water-photo{left:0;top:0;width:378px;height:380px;
  background:linear-gradient(180deg,#eef6c8 0%,#b9d95e 22%,#9cc84a 40%,#4aa3c9 62%,#1b78b8 82%,#2d8fcf 100%)}
.brand-title{left:0;top:38px;width:378px;font-family:"Questrial",sans-serif;color:var(--ink);text-align:center;font-weight:400}
.brand-title .name{display:block;font-size:36px;letter-spacing:.5px;line-height:1}
.brand-title .sub{display:block;font-size:18px;letter-spacing:.5px;margin-top:2px}
.service-line{left:0;top:108px;width:378px;text-align:center;font-size:12.5px;color:var(--ink)}
.service-line .dot{font-size:10px;margin:0 3px}
.brand-disc{left:134px;top:310px;width:104px;height:104px;border-radius:50%;background:var(--white);
  display:flex;align-items:center;justify-content:center;text-align:center;
  font-weight:700;font-size:11px;line-height:1.25;color:var(--deep);padding:10px}
.tagline{left:0;top:418px;width:378px;text-align:center;color:var(--navy)}
.tagline .t1{font-size:12.5px;color:var(--deep)}
.tagline .t2{font-size:11px}
.tagline .t2 b{font-size:13px}
.tagline .t3{font-size:13.5px;font-weight:700}
.region-line{left:0;top:478px;width:378px;text-align:center;font-size:9.5px;color:var(--ink)}
.region-line .dot{color:var(--deep)}
.contact-band{left:0;top:494px;width:378px;height:33px;background:linear-gradient(90deg,var(--lime),var(--leaf-soft));
  display:flex;align-items:center;justify-content:space-between;padding:0 10px;font-size:13.5px}
.contact-band .site{font-size:10px;color:var(--forest)}

/* ---------- inside spread ---------- */
.inside-bg{left:0;top:0;width:768px;height:526px;
  background:linear-gradient(90deg,#f2f6d4 0%,var(--white) 30%,var(--white) 50%,#eef4cc 70%,#f7f9e6 100%)}
.inside-header{left:0;top:0;width:768px;height:130px}
.section-title{font-family:"Questrial",sans-serif;font-size:27px;letter-spacing:.5px;font-weight:400}
.coaching-title{left:22px;top:26px;color:var(--white)}
.programs-title{left:402px;top:26px;color:var(--ink)}
.coaching-photo{left:186px;top:8px;width:189px;height:94px;background:linear-gradient(150deg,#3b2a22,#a98865 50%,#d9c7a7)}
.programs-photo{left:563px;top:7px;width:189px;height:78px;background:linear-gradient(160deg,#6e8a9e,#3b5b7c 45%,#9bb06a)}
.service-bar{height:19px;font-size:12.5px;font-weight:400;line-height:19px;border-radius:3px;
  font-family:"Questrial",sans-serif;background:linear-gradient(180deg,var(--leaf-soft),var(--leaf))}
.service-text{font-size:8px;line-height:1.17}
.service-text .lead{font-weight:700;font-style:italic;font-size:8.8px}
.col-left .service-bar,.col-left .service-text{left:35px;width:314px}
.col-right .service-bar{left:423px;width:312px}
.col-right .service-text{left:420px;width:320px}
.people-row{left:88px;top:440px;width:206px;height:30px;background:linear-gradient(90deg,#9aa7b8,#c9a15a,#6a8f4a,#b85e5e,#7c9cc4)}
.inside-url{left:60px;top:494px;width:254px;height:20px;line-height:20px}
.mail{color:var(--navy)}
.meaning-box{left:438px;top:410px;width:280px;height:36px;background:var(--ink);color:var(--white);text-align:center;border-radius:2px;padding-top:3px}
.meaning-box b{font-size:9.5px;display:block}
.meaning-box span{font-size:8px;display:block;line-height:1.15}
.partner-wave{left:384px;top:446px;width:384px;height:80px}
.partner-disc{left:444px;top:462px;width:52px;height:52px;border-radius:50%;background:var(--white);
  display:flex;align-items:center;justify-content:center;font-size:7px;font-weight:700;color:var(--deep);text-align:center;line-height:1.1}
.partner-text{left:510px;top:456px;width:240px;text-align:center;font-size:8.5px;line-height:1.15}
.partner-text .hl{font-weight:700;font-style:italic;color:var(--navy)}
.partner-text .big{font-weight:700;font-style:italic;font-size:10.5px;color:var(--navy)}
</style>
</head>
<body>

<section class="page page-cover" aria-label="Brochure cover spread">
  <div class="abs intro-panel">
    <div class="abs intro-sky"></div>
    <h1 class="abs intro-title center">MAY WE HELP YOU?</h1>
    <p class="abs intro-copy center">
      <span class="brand">Marlowe Vocation Advisors</span><br>
      <span class="soft">is working locally across the</span><br>
      Chesapeake Bay Watershed Region<br>
      <span class="soft">to cultivate " sustainable solutions"</span><br>
      <em>connecting partners with shared purpose</em><br>
      <em>matching Talent to Task</em><br>
      <em>achieving win/wins!</em>
    </p>
    <div class="abs intro-photo" role="img" aria-label="Photo of a smiling coach seated at a café table"></div>
    <svg class="abs swoosh" viewBox="0 0 390 80" preserveAspectRatio="none" aria-hidden="true">
      <path d="M0 30 C120 70 260 70 390 20 L390 80 L0 80 Z" fill="#f7f9e6"/>
      <path d="M0 34 C120 74 260 72 390 24" fill="none" stroke="#3d7d1f" stroke-width="5"/>
      <path d="M0 44 C140 80 270 78 390 34" fill="none" stroke="#a9cf55" stroke-width="3"/>
    </svg>

    <div class="abs label-bar coach-bar">Education/ Career/ Leadership/ Life<br>Transitions Coaching</div>
    <p class="abs team-list team-coach center">
      Ronda Kesterfield, Education/ Career/ Leadership Coach<br>
      Lorna Whitcombe, Professional Recruiter/ Career Coach<br>
      Greta Pellham, Executive Trainer/ Coach<br>
      Bea Norvale, Co-Active Life Coach
    </p>
    <h2 class="abs program-head center">VOCATERRANA:<br>Next Generation Leadership Development</h2>
    <p class="abs team-list team-program center">
      Ronda Kesterfield, Professional/ Experiential Programs<br>
      Lorna Whitcombe, Next Generation Corporate Programs<br>
      Tobias Wrenfield, CoSteward Leadership &amp; Innovation Training
    </p>

    <div class="abs call-box">
      <h3 class="abs call-head center">Free Friday Career Conference Calls</h3>
      <p class="abs call-info center">
        <b>Biweekly @ Noon-1pm</b><br>
        Conference Dial-in Number:<br>
        (555) 014-2290<br>
        Participant Access Code:<br>
        418207#
      </p>
      <div class="abs url-pill call-url">www.MarloweVocationAdvisors.com</div>
    </div>
  </div>

  <div class="abs cover-panel">
    <div class="abs water-photo" role="img" aria-label="Photo of a water droplet falling from a green leaf into a calm blue pool"></div>
    <h2 class="abs brand-title"><span class="name">MARLOWE</span><span class="sub">VOCATION ADVISORS</span></h2>
    <p class="abs service-line">Education<span class="dot">●</span> Career<span class="dot">●</span> Leadership<span class="dot">●</span> Coaching/ Programs</p>
    <div class="abs brand-disc">Marlowe Vocation Advisors</div>
    <p class="abs tagline">
      <span class="t1">Thinking Globally, Acting Locally</span><br>
      <span class="t2">to bring you <b>VocaTerrana</b></span><br>
      <span class="t3">Partners for a Sustainable Future</span>
    </p>
    <p class="abs region-line">Chesapeake Bay Watershed Region <span class="dot">●</span> DC Metro to Eastern Shore</p>
    <div class="abs contact-band">
      <span class="site">marlowevocationadvisors.com</span>
      <span>555-013-4471 <b>|</b> 555-019-8832</span>
    </div>
  </div>
</section>

<section class="page page-inside" aria-label="Brochure inside spread">
  <div class="abs inside-bg"></div>
  <svg class="abs inside-header" viewBox="0 0 768 130" preserveAspectRatio="none" aria-hidden="true">
    <defs>
      <linearGradient id="coach-band" x1="0" x2="1">
        <stop offset="0" stop-color="#2f6a14"/>
        <stop offset=".6" stop-color="#8cbf3f"/>
        <stop offset="1" stop-color="#d6e67a"/>
      </linearGradient>
    </defs>
    <path d="M0 0 H384 V70 C300 110 150 110 0 70 Z" fill="url(#coach-band)"/>
    <path d="M0 78 C150 118 300 118 384 78 C460 60 560 95 640 100 C700 104 740 95 768 85" fill="none" stroke="#3d7d1f" stroke-width="5"/>
    <path d="M0 90 C150 126 300 124 384 90 C470 72 560 108 650 110 C710 110 745 104 768 96" fill="none" stroke="#a9cf55" stroke-width="3"/>
  </svg>
  <h2 class="abs section-title coaching-title">COACHING</h2>
  <div class="abs coaching-photo" role="img" aria-label="Photo of a coach and client talking in a bookshop"></div>
  <h2 class="abs section-title programs-title">PROGRAMS</h2>
  <div class="abs programs-photo" role="img" aria-label="Photo of a field team of young professionals outdoors"></div>

  <div class="col-left">
    <h3 class="abs service-bar center" style="top:124px">Certified Professional Coaching</h3>
    <p class="abs service-text" style="top:146px">
      <span class="lead">Individual, customized, affordable</span> coaching for<br>
      <span class="lead">Education, Career, Life and Leadership Transitions</span><br>
      at varied stages of life and career challenges, to support achievement of personal and professional goals. We work with you in person, or flexibly by phone, email, Konferra. It is simple to get started ! Just contact us and we will customize affordable services and schedule adapted to your goals.
    </p>
    <h3 class="abs service-bar center" style="top:216px">Career &amp; Leadership Connections</h3>
    <p class="abs service-text" style="top:239px">
      <span class="lead">Group Coaching</span> and other program offerings can help build your network, while reducing the costs of individualized coaching, to proactively achieve your goals. Professionals exchange insights on career and organizational change management using a "coSteward" team assessment for innovation and change, providing mutual support as a team.
    </p>
    <h3 class="abs service-bar center" style="top:300px">Resumes, Covers, Interview Prep</h3>
    <p class="abs service-text" style="top:323px">
      <span class="lead">Your Professional Documents are customized,</span> so we offer the expertise of <span class="lead">Professional Resume Writers</span> and <span class="lead">Executive Recruiters</span> to prepare you for <span class="lead">Interviews</span> so you may land your next job! Fees may vary.
    </p>
    <h3 class="abs service-bar center" style="top:366px">Professional Branding/Portfolio</h3>
    <p class="abs service-text" style="top:389px">
      <span class="lead">Websites and Social Media Presence are a necessity</span><br>
      for contemporary job search, business development, and entrepreneurship. Consultants are ready to help you develop a webpage <span class="lead">Professional Portfolio to Market YOU</span>, your project or start-up enterprise.
    </p>
    <div class="abs people-row" role="img" aria-label="Illustration of a row of colourful standing figures"></div>
    <div class="abs url-pill inside-url">www.MarloweVocationAdvisors.com</div>
  </div>

  <div class="col-right">
    <h3 class="abs service-bar center" style="top:122px">VocaTerrana Community Course</h3>
    <p class="abs service-text" style="top:143px">
      <span class="lead">21<sup>st</sup> Century Career &amp; Leadership Development Course is delivered online with a team of certified coaches plus</span> international, interdisciplinary forum of professionals to help you get connected. We use easy, flexible technology to allow you to participate anytime, anywhere you connect to the internet! Course may be customized for varied curricula to integrate entrepreneurial motivation that supports achievement of individual, educational and/ or organizational goals.
    </p>
    <h3 class="abs service-bar center" style="top:216px">Workshops/ Seminars/ Networking</h3>
    <p class="abs service-text" style="top:237px">
      <span class="lead">There is really nothing like meeting in person</span> to combine benefits of coaching and networking with other professionals. We offer customized workshops for organizations and/ or opportunities throughout Chesapeake Bay Watershed Region from Washington DC to Eastern Shore for networking. We often host regional experts on contemporary issues impacting careers and leadership from urban to rural communities.
    </p>
    <h3 class="abs service-bar center" style="top:300px">Experiential/ Leadership Projects</h3>
    <p class="abs service-text" style="top:321px">
      <span class="lead">Experience is the best teacher for our Next Generation Professionals and Leaders.</span> We organize annual "<span class="lead">Marlowe Field Experiences</span>" to engage young professionals from top educational institutions, and partner with local leaders on projects focused on sustainable solutions building.
      <span class="lead">Do you have a project that could use fresh creative energy and skill ? Are you seeking project focused in sustainability to build expertise?</span>
      Please send your letter of interest, project description &amp;/ or resume to<br>
      <span class="mail">vocaterrana@marlowemail.net</span>
    </p>
    <div class="abs meaning-box">
      <b>What do we mean by Sustainability?</b>
      <span>We are committed to the long term health of our shared<br>natural environment, as well as individual futures, which requires</span>
    </div>
    <svg class="abs partner-wave" viewBox="0 0 384 80" preserveAspectRatio="none" aria-hidden="true">
      <path d="M0 22 C120 0 260 6 384 14 V80 H0 Z" fill="#d6e67a"/>
      <path d="M0 22 C120 0 260 6 384 14" fill="none" stroke="#8cbf3f" stroke-width="3"/>
    </svg>
    <div class="abs partner-disc">Marlowe Vocation Advisors</div>
    <p class="abs partner-text">
      <span class="hl">Community Partnerships</span> who<br>
      <span class="hl">THINK GLOBALLY &amp; ACT LOCALLY !</span><br>
      Overall, we seek to support mutual benefit of<br>
      <span class="big">People, Planet and Profit</span><br>
      as these all work together to ensure a better world<br>
      for future generations
    </p>
  </div>
</section>

</body>
</html>
```